Accounting business needs a fridge magnet design

I need a business card size design to be used as a fridge magnet.
It will need to be vertical not horizontal and it will have my logo and the services I provide listed below it.
It needs to be pleasing to the eye and catch peoples attention.
I have uploaded my current business card as a reference.
It can look totally different though, i am open to new ideas.

It will need to say:

Specialising in:
*Small Business Taxation
*Company & Trust Returns
*Financial Statements
*Partnership Taxation
*BAS preparation/lodgement
*Capital Gains Tax
*Business Start Ups
*Business Structuring
*Tax Planning

```html
<!DOCTYPE html>
<html lang="en">
<head>
<meta charset="UTF-8">
<title>Nova Tax – Fridge Magnet</title>
<link href="https://fonts.googleapis.com/css2?family=Montserrat:wght@500&family=Poppins:wght@400;600&family=Roboto:wght@400&display=swap" rel="stylesheet">
<style>
  :root {
    --page-bg: #e4e4e4;
    --card-white: #ffffff;
    --ink: #2a2b2d;
    --band: #2b2c2e;
    --band-text: #ffffff;
    --lime: #c4d600;
    --ring: #6e6e6e;
  }
  html, body {
    margin: 0;
    padding: 0;
    width: 1200px;
    height: 1200px;
    overflow: hidden;
    background: var(--page-bg);
  }
  .canvas {
    position: relative;
    width: 1200px;
    height: 1200px;
  }
  .magnet {
    position: absolute;
    left: 330px;
    top: 160px;
    width: 540px;
    height: 880px;
    background: var(--card-white);
    display: flex;
    flex-direction: column;
  }
  .brand {
    height: 321px;
    display: flex;
    flex-direction: column;
    align-items: center;
  }
  .brand-circle {
    margin-top: 62px;
    width: 142px;
    height: 142px;
    border: 3px solid var(--ink);
    border-radius: 50%;
    box-sizing: border-box;
  }
  .brand-name {
    margin-top: 30px;
    font-family: "Montserrat", sans-serif;
    font-weight: 500;
    font-size: 44px;
    letter-spacing: 0.42em;
    margin-right: -0.42em;
    color: var(--ink);
    line-height: 1;
  }
  .services {
    height: 362px;
    background: var(--band);
    color: var(--band-text);
    font-family: "Poppins", sans-serif;
    text-align: center;
    box-sizing: border-box;
    padding-top: 16px;
  }
  .services-heading {
    margin: 0;
    font-weight: 600;
    font-size: 23px;
    line-height: 32px;
  }
  .services-list {
    list-style: none;
    margin: 14px 0 0;
    padding: 0;
    font-weight: 400;
    font-size: 24px;
    line-height: 31px;
  }
  .registration {
    height: 179px;
    display: flex;
    flex-direction: column;
    align-items: center;
  }
  .registration-badge {
    margin-top: 21px;
  }
  .agent-number {
    margin-top: 6px;
    font-family: "Roboto", sans-serif;
    font-size: 13px;
    line-height: 16px;
    color: var(--ink);
    text-align: center;
  }
  .accent-bar {
    height: 18px;
    background: var(--lime);
  }
</style>
</head>
<body>
<div class="canvas">
  <div class="magnet">
    <header class="brand">
      <div class="brand-circle"></div>
      <div class="brand-name">NOVA TAX</div>
    </header>

    <section class="services">
      <h2 class="services-heading">SPECIALISING IN:</h2>
      <ul class="services-list">
        <li>SMALL BUSINESS TAXATION</li>
        <li>COMPANY &amp; TRUST RETURNS</li>
        <li>FINANCIAL STATEMENTS</li>
        <li>PARTNERSHIP TAXATION</li>
        <li>BAS PREPARATION/LODGEMENT</li>
        <li>CAPITAL GAINS TAX</li>
        <li>BUSINESS START UPS</li>
        <li>BUSINESS STRUCTURING</li>
        <li>TAX PLANNING</li>
      </ul>
    </section>

    <footer class="registration">
      <svg class="registration-badge" width="104" height="104" viewBox="0 0 104 104" role="img" aria-label="Registration badge">
        <circle cx="52" cy="52" r="50" fill="#ffffff" stroke="var(--ring)" stroke-width="1.5"/>
        <circle cx="52" cy="52" r="30" fill="var(--lime)"/>
      </svg>
      <div class="agent-number">Tax agent<br>48213905</div>
    </footer>

    <div class="accent-bar"></div>
  </div>
</div>
</body>
</html>
```